KV MACHINERY DEPOT

we sell used heavy equipment look at our current website www.halvardhauling.com we are looking for a easier site to use with our new name

```html
<!DOCTYPE html>
<html lang="en">
<head>
<meta charset="utf-8">
<title>KV Machinery Depot – Used Heavy Construction Equipment</title>
<link rel="stylesheet" href="https://fonts.googleapis.com/css2?family=Exo+2:wght@700;800&family=Montserrat:wght@400;500;600;700&display=swap">
<style>
:root{
  --blue:#22418f;
  --blue-dark:#1b3577;
  --brown:#8b6a3a;
  --brown-dark:#6e5230;
  --pale:#eaf0f8;
  --ink:#2b2b2b;
  --muted:#555;
  --white:#fff;
}
*{box-sizing:border-box;margin:0;padding:0}
html,body{width:1200px;height:4187px;overflow:hidden}
body{position:relative;font-family:"Montserrat",sans-serif;color:var(--ink);background:var(--white)}
.abs{position:absolute}
a{color:inherit;text-decoration:none}
.btn{position:absolute;display:flex;align-items:center;justify-content:center;gap:8px;border-radius:30px;font-weight:600;font-size:17px;letter-spacing:.5px}
.btn-brown{background:var(--brown);color:var(--white)}
.btn-blue{background:var(--blue);color:var(--white)}
.btn-outline-white{border:2px solid rgba(255,255,255,.8);color:var(--white)}
.btn-outline-blue{border:2px solid var(--blue);color:var(--blue);background:var(--white)}
.chev{font-size:15px}

.site-header{position:absolute;left:0;top:0;width:1200px;height:114px;background:var(--white);z-index:3}
.logo-badge{position:absolute;left:80px;top:0;width:232px;height:163px;background:var(--white);border-radius:0 0 116px 116px / 0 0 60px 60px;z-index:4;display:flex;flex-direction:column;align-items:center;justify-content:center;gap:8px;padding-top:10px}
.logo-dot{width:30px;height:30px;border-radius:50%;background:var(--brown)}
.logo-name{font-weight:700;font-size:17px;color:var(--blue);letter-spacing:.5px;text-align:center;line-height:1.2}
.topbar{position:absolute;top:14px;right:108px;display:flex;gap:28px;font-size:15px;color:var(--blue)}
.topbar span{display:flex;align-items:center;gap:9px}
.mainnav{position:absolute;top:68px;left:343px;display:flex;gap:38px;font-size:14px;font-weight:600;color:var(--blue)}
.quote{left:970px;top:56px;width:156px;height:42px;font-size:14px;font-weight:500}

.hero{position:absolute;left:0;top:114px;width:1200px;height:637px;background:linear-gradient(90deg,#22418f 0%,#2a4b97 40%,#5d78b3 70%,#8fa3c8 100%);overflow:hidden}
.hero-photo{position:absolute;left:470px;top:0;width:730px;height:637px;background:linear-gradient(135deg,rgba(160,175,205,.3),rgba(205,110,40,.55) 45%,rgba(60,60,60,.6) 70%,rgba(200,195,185,.7))}
.hero-tag{position:absolute;left:101px;top:252px;height:38px;padding:0 16px;background:var(--brown);color:var(--white);font-family:"Exo 2",sans-serif;font-weight:700;font-size:22px;letter-spacing:2px;display:flex;align-items:center}
.hero-title{position:absolute;left:101px;top:300px;font-family:"Exo 2",sans-serif;font-weight:800;font-size:54px;line-height:57px;color:var(--white);letter-spacing:1px}

.about-frame{position:absolute;left:76px;top:822px;width:282px;height:247px;background:var(--brown)}
.about-frame-inner{position:absolute;left:88px;top:834px;width:490px;height:420px;background:var(--white)}
.about-photo{position:absolute;left:98px;top:841px;width:466px;height:420px;background:linear-gradient(180deg,#b8c6d6 0%,#d9dcd8 35%,#7e7a5c 55%,#5c4630 80%,#3f3122 100%)}
.about-bar{position:absolute;left:564px;top:857px;width:5px;height:150px;background:var(--blue)}
.eyebrow{font-size:17px;letter-spacing:2px;color:var(--blue);font-weight:500}
.h2-brown{font-weight:700;color:var(--brown)}
.h2-blue{font-weight:700;color:var(--blue)}
.rule{position:absolute;width:74px;height:4px;background:var(--brown);border-radius:2px}
.about-text{position:absolute;left:630px;top:1000px;width:520px;font-size:18.5px;line-height:29.5px;color:var(--ink)}

.products-band{position:absolute;left:0;top:1364px;width:1200px;height:465px;background:linear-gradient(180deg,#9a7642,#8b6a3a 60%,#7b5d33)}
.products-eyebrow{position:absolute;left:0;top:1440px;width:1200px;text-align:center;color:var(--white);font-size:19px;letter-spacing:3px}
.products-title{position:absolute;left:0;top:1473px;width:1200px;text-align:center;color:var(--white);font-weight:700;font-size:31px;line-height:38px}
.slide-arrow{position:absolute;top:1718px;width:32px;height:56px}
.card{position:absolute;top:1611px;width:324px;height:524px;background:var(--white);border:1px solid #cfd6e4}
.card-photo{position:absolute;left:0;top:0;width:100%;height:218px}
.card-title{position:absolute;left:26px;top:236px;font-weight:700;font-size:19px;line-height:24px;color:var(--blue)}
.spec{position:absolute;display:flex;gap:8px;font-size:11px;line-height:14px;color:var(--ink)}
.spec b{display:block;font-weight:600}
.spec svg{flex:none;margin-top:2px}
.card .btn{border-radius:0;font-size:13px;height:39px;top:469px}
.card .buy{left:22px;width:139px}
.card .view{left:169px;width:142px;border:2px solid var(--blue);color:var(--blue);background:var(--white)}
.view-more{left:494px;top:2195px;width:207px;height:55px}

.trade{position:absolute;left:0;top:2304px;width:1200px;height:745px;background:var(--pale)}
.trade-photo{position:absolute;top:2367px;width:470px;height:327px}
.trade-card{position:absolute;top:2585px;width:418px;height:321px;background:var(--white);clip-path:polygon(0 10%,100% 0,100% 100%,0 100%)}
.trade-icon{position:absolute;width:104px;height:104px;border-radius:50%;display:flex;align-items:center;justify-content:center}
.trade h3{position:absolute;font-weight:700;font-size:24px;color:var(--ink);letter-spacing:.5px}
.trade-text{position:absolute;font-size:15px;line-height:19px;color:var(--muted)}

.finance{position:absolute;left:127px;top:2961px;width:979px;height:221px;background:linear-gradient(90deg,#22418f,#2a4c97 50%,#22418f)}
.finance-inner{position:absolute;left:13px;top:13px;right:13px;bottom:13px;border:1.5px solid rgba(255,255,255,.6)}
.finance h2{position:absolute;left:0;top:58px;width:100%;text-align:center;color:var(--white);font-weight:700;font-size:29px}
.finance p{position:absolute;left:0;top:99px;width:100%;text-align:center;color:var(--white);font-size:17px;letter-spacing:2.5px;font-weight:500}
.finance .btn{left:398px;top:130px;width:179px;height:44px;font-size:15px}

.contact-item{position:absolute;left:145px;display:flex;align-items:center;gap:22px;font-size:20px;line-height:28px;color:var(--ink)}
.contact-icon{width:48px;height:48px;border-radius:50%;background:var(--blue);display:flex;align-items:center;justify-content:center;flex:none}
.form-box{position:absolute;left:611px;top:3265px;width:483px;height:426px;background:var(--brown)}
.field{position:absolute;background:var(--white);display:flex;align-items:center;gap:9px;padding-left:18px;font-size:13px;color:#444}
.field.textarea{align-items:flex-start;padding-top:14px}
.send{left:647px;top:3613px;width:203px;height:46px;font-size:15px}

.site-footer{position:absolute;left:0;top:3777px;width:1200px;height:410px;background:var(--blue);color:var(--white)}
.footer-logo{position:absolute;left:122px;top:60px;width:228px;display:flex;flex-direction:column;align-items:center;gap:12px}
.footer-logo .logo-dot{width:40px;height:40px;background:var(--white)}
.footer-logo .logo-name{color:var(--white);font-size:19px}
.socials{position:absolute;left:176px;top:241px;display:flex;gap:6px}
.socials span{width:28px;height:28px;border-radius:50%;background:var(--white)}
.fcol{position:absolute;top:80px}
.fcol h4{font-size:18px;font-weight:600;letter-spacing:.5px;margin-bottom:16px}
.fcol li{list-style:none;font-size:13px;line-height:23.3px}
.fline{display:flex;gap:12px;font-size:13px;line-height:19px;margin-bottom:12px}
.footer-rule{position:absolute;left:0;top:332px;width:1200px;height:1px;background:rgba(255,255,255,.35)}
.copyright{position:absolute;left:0;top:358px;width:1190px;text-align:center;font-size:13px}
.to-top{position:absolute;left:1026px;top:346px}
</style>
</head>
<body>

<header class="site-header">
  <div class="topbar">
    <span><svg width="22" height="22" viewBox="0 0 22 22"><circle cx="11" cy="11" r="11" fill="#22418f"/><rect x="5.5" y="7" width="11" height="8" rx="1" fill="none" stroke="#fff" stroke-width="1.4"/><path d="M5.5 7.5l5.5 4 5.5-4" fill="none" stroke="#fff" stroke-width="1.4"/></svg>sales@kvmachinerydepot.com</span>
    <span><svg width="22" height="22" viewBox="0 0 22 22"><circle cx="11" cy="11" r="11" fill="#8b6a3a"/><path d="M7.5 6.2l2 .2.8 2.3-1.3 1a6 6 0 003.3 3.3l1-1.3 2.3.8.2 2c-.6.9-1.6 1.2-2.6.9-3.2-1-5.7-3.5-6.7-6.7-.3-1 0-2 1-2.5z" fill="#fff"/></svg>CALL US: (555) 014-2280</span>
  </div>
  <nav class="mainnav">
    <a>USED CONSTRUCTION EQUIPMENT</a><a>FINANCING</a><a>APPLY NOW</a><a>ABOUT US</a>
  </nav>
  <a class="btn btn-brown quote">GET A QUOTE <span class="chev">›</span></a>
</header>
<div class="logo-badge">
  <div class="logo-dot"></div>
  <div class="logo-name">KV MACHINERY DEPOT</div>
</div>

<section class="hero">
  <div class="hero-photo" role="img" aria-label="Orange telehandler with extended boom parked at a construction site"></div>
</section>
<div class="hero-tag">KV MACHINERY DEPOT</div>
<h1 class="hero-title">USED HEAVY<br>CONSTRUCTION<br>EQUIPMENT SALES</h1>
<a class="btn btn-brown" style="left:98px;top:491px;width:206px;height:55px">LEARN MORE <span class="chev">›</span></a>
<a class="btn btn-outline-white" style="left:319px;top:491px;width:260px;height:55px;font-weight:500">FINANCE AVALIABLE <span class="chev">›</span></a>

<div class="about-frame"></div>
<div class="about-frame-inner"></div>
<div class="about-photo" role="img" aria-label="Compact telehandler lifting material on a farm yard"></div>
<div class="about-bar"></div>
<div class="abs eyebrow" style="left:629px;top:853px">OUR COMPANY</div>
<div class="abs h2-brown" style="left:629px;top:878px;font-size:39px;line-height:44px">ABOUT KV</div>
<div class="abs h2-blue" style="left:629px;top:922px;font-size:39px;line-height:44px">MACHINERY DEPOT</div>
<div class="rule" style="left:631px;top:979px"></div>
<p class="about-text">We understand the challenges and obstacles of purchasing cheap used construction equipment for sale, especially in California. Moreover, our goal is to provide a seamless and reliable experience for our customers. Though, ensure that you find the right equipment and receive it on time, every time.</p>
<a class="btn btn-outline-blue" style="left:623px;top:1206px;width:206px;height:54px">LEARN MORE <span class="chev">›</span></a>

<div class="products-band" role="img" aria-label="Brown tinted photo of a work site behind the equipment listings"></div>
<div class="products-eyebrow">THE BEST COST USED EQUIPMENTS</div>
<h2 class="products-title">THE CONSTRUCTION EQUIPMENT WITH LOW<br>COST FOR SAVING YOUR BUDGET</h2>
<div class="rule" style="left:563px;top:1564px;background:#fff"></div>
<svg class="slide-arrow" style="left:34px" viewBox="0 0 32 56"><path d="M28 3L4 28l24 25" fill="none" stroke="#fff" stroke-width="3"/></svg>
<svg class="slide-arrow" style="left:1138px" viewBox="0 0 32 56"><path d="M4 3l24 25L4 53" fill="none" stroke="#fff" stroke-width="3"/></svg>

<article class="card" style="left:102px">
  <div class="card-photo" role="img" aria-label="Orange telehandler parked in a yard" style="background:linear-gradient(180deg,#b9c9d8,#d0874a 55%,#4a4a46)"></div>
  <h3 class="card-title">2015 Torvane T42<br>Telehandler</h3>
  <div class="spec" style="left:26px;top:296px"><svg width="18" height="18"><circle cx="9" cy="9" r="7" fill="none" stroke="#8aa0c8" stroke-width="1.5"/></svg><div><b>Availability:</b>In Stock</div></div>
  <div class="spec" style="left:163px;top:299px"><svg width="18" height="18"><circle cx="9" cy="6" r="4" fill="none" stroke="#8aa0c8" stroke-width="1.5"/><path d="M2 17c1-5 13-5 14 0" fill="none" stroke="#8aa0c8" stroke-width="1.5"/></svg><div><b>Make:</b>Torvane</div></div>
  <div class="spec" style="left:26px;top:346px"><svg width="18" height="18"><path d="M3 5h12M3 9h12M3 13h12" stroke="#8aa0c8" stroke-width="1.5"/></svg><div><b>Model:</b>T42</div></div>
  <div class="spec" style="left:163px;top:346px"><svg width="22" height="18"><rect x="1" y="9" width="12" height="6" fill="none" stroke="#8aa0c8" stroke-width="1.5"/><path d="M8 9L19 2" stroke="#8aa0c8" stroke-width="1.5"/></svg><div><b>Vehicle type:</b>42 ft reach<br>3200 hrs</div></div>
  <div class="spec" style="left:26px;top:396px"><svg width="18" height="18"><path d="M4 16l3-11h4l3 11z" fill="none" stroke="#8aa0c8" stroke-width="1.5"/></svg><div><b>Weight:</b>4 8000 lbs</div></div>
  <div class="spec" style="left:163px;top:406px"><svg width="18" height="18"><rect x="1" y="5" width="10" height="8" fill="#8aa0c8"/><rect x="11" y="8" width="5" height="5" fill="#8aa0c8"/></svg><div><b>Shipping:</b>Shipping nationwide</div></div>
  <div class="spec" style="left:26px;top:434px"><svg width="18" height="18"><rect x="2" y="3" width="14" height="13" fill="none" stroke="#8aa0c8" stroke-width="1.5"/><path d="M2 7h14" stroke="#8aa0c8" stroke-width="1.5"/></svg><div style="padding-top:3px"><b>Year: 2015</b></div></div>
  <a class="btn btn-brown buy">BUY NOW <span class="chev">›</span></a>
  <a class="btn view">VIEW DETAIL <span class="chev">›</span></a>
</article>

<article class="card" style="left:446px">
  <div class="card-photo" role="img" aria-label="Yellow skip loader tractor parked on a dirt lot" style="background:linear-gradient(180deg,#a9c4dc,#c9a84a 55%,#5c5a4a)"></div>
  <h3 class="card-title">2015 Brakwell B21<br>Skip loader</h3>
  <div class="spec" style="left:26px;top:296px"><svg width="18" height="18"><circle cx="9" cy="9" r="7" fill="none" stroke="#8aa0c8" stroke-width="1.5"/></svg><div><b>Availability:</b>In Stock</div></div>
  <div class="spec" style="left:163px;top:299px"><svg width="18" height="18"><circle cx="9" cy="6" r="4" fill="none" stroke="#8aa0c8" stroke-width="1.5"/><path d="M2 17c1-5 13-5 14 0" fill="none" stroke="#8aa0c8" stroke-width="1.5"/></svg><div><b>Make:</b>Torvane</div></div>
  <div class="spec" style="left:26px;top:346px"><svg width="18" height="18"><path d="M3 5h12M3 9h12M3 13h12" stroke="#8aa0c8" stroke-width="1.5"/></svg><div><b>Model:</b>T42</div></div>
  <div class="spec" style="left:163px;top:346px"><svg width="22" height="18"><rect x="1" y="9" width="12" height="6" fill="none" stroke="#8aa0c8" stroke-width="1.5"/><path d="M8 9L19 2" stroke="#8aa0c8" stroke-width="1.5"/></svg><div><b>Vehicle type:</b>42 ft reach<br>3200 hrs</div></div>
  <div class="spec" style="left:26px;top:396px"><svg width="18" height="18"><path d="M4 16l3-11h4l3 11z" fill="none" stroke="#8aa0c8" stroke-width="1.5"/></svg><div><b>Weight:</b>4 8000 lbs</div></div>
  <div class="spec" style="left:163px;top:406px"><svg width="18" height="18"><rect x="1" y="5" width="10" height="8" fill="#8aa0c8"/><rect x="11" y="8" width="5" height="5" fill="#8aa0c8"/></svg><div><b>Shipping:</b>Shipping nationwide</div></div>
  <div class="spec" style="left:26px;top:434px"><svg width="18" height="18"><rect x="2" y="3" width="14" height="13" fill="none" stroke="#8aa0c8" stroke-width="1.5"/><path d="M2 7h14" stroke="#8aa0c8" stroke-width="1.5"/></svg><div style="padding-top:3px"><b>Year: 2015</b></div></div>
  <a class="btn btn-brown buy">BUY NOW <span class="chev">›</span></a>
  <a class="btn view">VIEW DETAIL <span class="chev">›</span></a>
</article>

<article class="card" style="left:798px">
  <div class="card-photo" role="img" aria-label="Orange telehandler with raised boom on a paved lot" style="background:linear-gradient(180deg,#b4cde6,#d9772f 50%,#6f6d66)"></div>
  <h3 class="card-title">2015 Ostrem OX105<br>Telehandler</h3>
  <div class="spec" style="left:26px;top:296px"><svg width="18" height="18"><circle cx="9" cy="9" r="7" fill="none" stroke="#8aa0c8" stroke-width="1.5"/></svg><div><b>Availability:</b>In Stock</div></div>
  <div class="spec" style="left:163px;top:299px"><svg width="18" height="18"><circle cx="9" cy="6" r="4" fill="none" stroke="#8aa0c8" stroke-width="1.5"/><path d="M2 17c1-5 13-5 14 0" fill="none" stroke="#8aa0c8" stroke-width="1.5"/></svg><div><b>Make:</b>Torvane</div></div>
  <div class="spec" style="left:26px;top:346px"><svg width="18" height="18"><path d="M3 5h12M3 9h12M3 13h12" stroke="#8aa0c8" stroke-width="1.5"/></svg><div><b>Model:</b>T42</div></div>
  <div class="spec" style="left:163px;top:346px"><svg width="22" height="18"><rect x="1" y="9" width="12" height="6" fill="none" stroke="#8aa0c8" stroke-width="1.5"/><path d="M8 9L19 2" stroke="#8aa0c8" stroke-width="1.5"/></svg><div><b>Vehicle type:</b>42 ft reach<br>3200 hrs</div></div>
  <div class="spec" style="left:26px;top:396px"><svg width="18" height="18"><path d="M4 16l3-11h4l3 11z" fill="none" stroke="#8aa0c8" stroke-width="1.5"/></svg><div><b>Weight:</b>4 8000 lbs</div></div>
  <div class="spec" style="left:163px;top:406px"><svg width="18" height="18"><rect x="1" y="5" width="10" height="8" fill="#8aa0c8"/><rect x="11" y="8" width="5" height="5" fill="#8aa0c8"/></svg><div><b>Shipping:</b>Shipping nationwide</div></div>
  <div class="spec" style="left:26px;top:434px"><svg width="18" height="18"><rect x="2" y="3" width="14" height="13" fill="none" stroke="#8aa0c8" stroke-width="1.5"/><path d="M2 7h14" stroke="#8aa0c8" stroke-width="1.5"/></svg><div style="padding-top:3px"><b>Year: 2015</b></div></div>
  <a class="btn btn-brown buy">BUY NOW <span class="chev">›</span></a>
  <a class="btn view">VIEW DETAIL <span class="chev">›</span></a>
</article>

<a class="btn btn-blue view-more">VIEW MORE <span class="chev">›</span></a>

<section class="trade">
  <div class="trade-photo" style="left:106px;top:63px;background:linear-gradient(180deg,#aec6de,#d6b64c 55%,#6a6a66)" role="img" aria-label="Yellow backhoe loader parked on a street"></div>
  <div class="trade-photo" style="left:623px;top:63px;background:linear-gradient(180deg,#b7cbe0,#c9a64a 50%,#5e5c56)" role="img" aria-label="Yellow telehandler parked at an equipment yard"></div>
  <div class="trade-card" style="left:135px;top:281px"></div>
  <div class="trade-card" style="left:650px;top:281px"></div>
  <div class="trade-icon" style="left:184px;top:250px;background:var(--brown)">
    <svg width="54" height="46" viewBox="0 0 54 46" fill="none" stroke="#fff" stroke-width="2"><rect x="6" y="20" width="22" height="12"/><rect x="12" y="10" width="10" height="10"/><circle cx="12" cy="38" r="5"/><circle cx="26" cy="38" r="5"/><path d="M28 22l12-14 8 10-4 8"/></svg>
  </div>
  <div class="trade-icon" style="left:697px;top:250px;background:var(--blue)">
    <svg width="54" height="46" viewBox="0 0 54 46" fill="none" stroke="#fff" stroke-width="2"><rect x="6" y="20" width="22" height="12"/><rect x="12" y="10" width="10" height="10"/><circle cx="12" cy="38" r="5"/><circle cx="26" cy="38" r="5"/><path d="M28 22l12-14 8 10-4 8"/></svg>
  </div>
  <h3 style="left:184px;top:370px">LOOKING TO BUY?</h3>
  <p class="trade-text" style="left:184px;top:413px;width:330px">We find the BEST preowned or new equip-ment for our customers. Let us know what you are looking for, what price range and we will get it for you!</p>
  <h3 style="left:700px;top:370px">WANT TO SELL?</h3>
  <p class="trade-text" style="left:700px;top:412px;width:345px;font-size:13.5px">Receive the absolute best value for your trade-in equipment. We even handle all paperwork. Call us to schedule an appointment or fill out the form below and we will find you a buyer!</p>
  <a class="btn btn-brown" style="left:172px;top:511px;width:234px;height:55px">BUY EQUIPMENT <span class="chev">›</span></a>
  <a class="btn btn-blue" style="left:688px;top:509px;width:234px;height:55px">SELL EQUIPMENT <span class="chev">›</span></a>
</section>

<section class="finance">
  <div class="finance-inner"></div>
  <h2>FINANCE OPTION AVAILABLE</h2>
  <p>GET FINANCE YOUR EQUIPMENT</p>
  <a class="btn btn-brown">CLICK HERE <span class="chev">›</span></a>
</section>

<div class="abs eyebrow" style="left:141px;top:3287px;color:var(--ink)">CONTACT US</div>
<div class="abs h2-brown" style="left:141px;top:3312px;font-size:42px;line-height:48px">GET IN TOUCH</div>
<div class="abs h2-blue" style="left:141px;top:3360px;font-size:42px;line-height:48px">WITH US</div>
<div class="rule" style="left:143px;top:3418px"></div>

<div class="contact-item" style="top:3459px">
  <span class="contact-icon"><svg width="20" height="24" viewBox="0 0 20 24"><path d="M10 1a8 8 0 018 8c0 6-8 14-8 14S2 15 2 9a8 8 0 018-8z" fill="#fff"/><circle cx="10" cy="9" r="3" fill="#22418f"/></svg></span>
  <span>4820 Ridgeline Road,<br>Alder Springs CA 90410</span>
</div>
<div class="contact-item" style="top:3535px">
  <span class="contact-icon"><svg width="22" height="22" viewBox="0 0 22 22"><path d="M5 3l4 .4 1.5 4.5-2.5 2a11 11 0 006 6l2-2.5 4.5 1.5.4 4c-1 1.6-3 2.3-5 1.6C9.5 18.6 5.4 14.5 3.5 8.5 2.8 6.5 3.4 4.2 5 3z" fill="#fff"/></svg></span>
  <span>Phone: (555) 014-2280</span>
</div>
<div class="contact-item" style="top:3601px">
  <span class="contact-icon"><svg width="24" height="18" viewBox="0 0 24 18"><rect x="1" y="1" width="22" height="16" rx="2" fill="none" stroke="#fff" stroke-width="2"/><path d="M2 2l10 8 10-8" fill="none" stroke="#fff" stroke-width="2"/></svg></span>
  <span>sales@kvmachinerydepot.com</span>
</div>

<form class="form-box">
  <div class="field" style="left:43px;top:42px;width:198px;height:46px"><svg width="12" height="13"><circle cx="6" cy="4" r="3" fill="#999"/><path d="M0 13c1-5 11-5 12 0z" fill="#999"/></svg>First Name*</div>
  <div class="field" style="left:249px;top:42px;width:200px;height:46px"><svg width="12" height="13"><circle cx="6" cy="4" r="3" fill="#999"/><path d="M0 13c1-5 11-5 12 0z" fill="#999"/></svg>Last Name*</div>
  <div class="field" style="left:43px;top:103px;width:406px;height:47px"><svg width="14" height="10"><rect x=".5" y=".5" width="13" height="9" fill="none" stroke="#999"/><path d="M1 1l6 5 6-5" fill="none" stroke="#999"/></svg>Email address*</div>
  <div class="field" style="left:43px;top:168px;width:406px;height:47px"><svg width="12" height="12"><path d="M2 1l3 .3 1 3-1.5 1.2a7 7 0 003 3L9 7l3 1 .2 3c-.8 1-2 1.2-3 .8A11 11 0 011 4c-.3-1.2 0-2.4 1-3z" fill="#999"/></svg>Phone*</div>
  <div class="field textarea" style="left:43px;top:231px;width:406px;height:102px"><svg width="14" height="12"><ellipse cx="7" cy="5" rx="7" ry="5" fill="#999"/></svg>Leave Message</div>
</form>
<a class="btn btn-blue send">SEND MESSAGE</a>

<footer class="site-footer">
  <div class="footer-logo">
    <div class="logo-dot"></div>
    <div class="logo-name">KV MACHINERY DEPOT</div>
  </div>
  <div class="socials" aria-label="Social links"><span></span><span></span><span></span><span></span></div>

  <div class="fcol" style="left:416px">
    <h4>NAVIGATION</h4>
    <ul>
      <li>Used construction equipment</li><li>Get a quote</li><li>Financing</li><li>Apply now</li><li>Our goal</li><li>About us</li>
    </ul>
  </div>
  <div class="fcol" style="left:655px;top:78px">
    <h4>BUSINESS HOURS</h4>
    <p class="fline" style="display:block">Monday - Friday:<br>7:00 AM – 3:30 PM</p>
    <p class="fline" style="display:block;margin-top:22px">Saturday &amp; Sunday:<br>Closed</p>
  </div>
  <div class="fcol" style="left:858px;top:78px">
    <h4>CONTACT US</h4>
    <div class="fline"><svg width="14" height="17" viewBox="0 0 20 24"><path d="M10 1a8 8 0 018 8c0 6-8 14-8 14S2 15 2 9a8 8 0 018-8z" fill="#fff"/></svg><span>4820 Ridgeline Road,<br>Alder Springs CA 90410</span></div>
    <div class="fline"><svg width="15" height="12" viewBox="0 0 24 18"><rect x="1" y="1" width="22" height="16" rx="2" fill="none" stroke="#fff" stroke-width="2.5"/><path d="M2 2l10 8 10-8" fill="none" stroke="#fff" stroke-width="2.5"/></svg><span>sales@kvmachinerydepot.com</span></div>
    <div class="fline"><svg width="14" height="14" viewBox="0 0 22 22"><path d="M5 3l4 .4 1.5 4.5-2.5 2a11 11 0 006 6l2-2.5 4.5 1.5.4 4c-1 1.6-3 2.3-5 1.6C9.5 18.6 5.4 14.5 3.5 8.5 2.8 6.5 3.4 4.2 5 3z" fill="#fff"/></svg><span>(555) 014-2280</span></div>
    <div class="fline"><svg width="15" height="15" viewBox="0 0 16 16" fill="none" stroke="#fff" stroke-width="1.3"><circle cx="8" cy="8" r="7"/><ellipse cx="8" cy="8" rx="3" ry="7"/><path d="M1 8h14"/></svg><span>www.halvardhauling.com</span></div>
  </div>

  <div class="footer-rule"></div>
  <p class="copyright">Copyright © 2024 KV Machinery Depot. All Right Reserved</p>
  <svg class="to-top" width="18" height="28" viewBox="0 0 18 28"><path d="M9 26V3M2 10l7-7 7 7" fill="none" stroke="#fff" stroke-width="2"/></svg>
</footer>

</body>
</html>
```